Copper Wren Beverage Co.

Copper Wren is a new beverage company that currently specializes in energy and hydration. I need label design for the bottles. The label will be a full sleeve so free free to use the entire bottle. The premise behind the product is that its a Copper Wren from the competition. The label needs to say smart, strong, expensive. The background for the label will be black.
Updates

I need an entire label design as well as logo

Target Market(s)

20-30 year old active people.

Industry/Entity Type

It Company

Logo Text

By athletes for the athlete in all of us.

Logo styles of interest
Pictorial/Combination Logo
Wordmark Logo
Requirements
Must have
• the flavors are fruit based. Blackberry lime, mango pineapple, mango berry, strawberry kiwi. Incorporate natural looking fruit into the design.

```html
<!DOCTYPE html>
<html lang="en">
<head>
<meta charset="utf-8">
<title>Copper Wren – Natural Energy Drink Labels</title>
<link href="https://fonts.googleapis.com/css2?family=Montserrat:wght@600;800;900&display=swap" rel="stylesheet">
<style>
  :root {
    --bg: #000000;
    --sleeve: #1b1b1c;
    --sleeve-edge: #2a2a2b;
    --white: #f4f4f4;
    --muted: #8a8a8a;
    --mango: #f2d83a;
    --mango-deep: #e6b81c;
    --berry: #8e3aa0;
    --berry-deep: #5a2a63;
    --lime: #9ad43a;
    --kiwi: #7fb83a;
    --strawberry: #ec3a3a;
    --strawberry-deep: #c8202b;
  }
  * { box-sizing: border-box; margin: 0; padding: 0; }
  html, body { width: 1200px; height: 900px; overflow: hidden; background: var(--bg); }
  body { font-family: "Montserrat", Arial, sans-serif; position: relative; }

  .brand-mark {
    position: absolute; top: 48px; left: 0; width: 1200px;
    text-align: center; color: var(--mango);
    font-weight: 900; font-size: 56px; line-height: 0.95; letter-spacing: 1px;
  }

  .sleeve {
    position: absolute; top: 228px; width: 212px; height: 560px;
    background: var(--sleeve); border: 1px solid var(--sleeve-edge); border-radius: 8px;
    overflow: hidden;
  }
  .sleeve--mango { left: 164px; --accent: var(--mango); --accent-text: #1b1b1c; }
  .sleeve--berry { left: 494px; --accent: var(--berry); --accent-text: var(--white); }
  .sleeve--kiwi  { left: 829px; --accent: var(--strawberry); --accent-text: var(--white); }

  .sleeve__tagline {
    position: absolute; top: 52px; width: 100%; text-align: center;
    color: var(--white); font-weight: 800; font-size: 9px; line-height: 1.2;
  }

  .sleeve__fruit {
    position: absolute; top: 112px; left: 46px; width: 120px; height: 370px;
    border-radius: 40px;
  }
  .sleeve--mango .sleeve__fruit { background: linear-gradient(180deg, #c9a33a, #e8cf5a 45%, #9a8a2e 80%, #7a6a2a); }
  .sleeve--berry .sleeve__fruit { background: linear-gradient(180deg, #3a2a44, #a8d84a 40%, #3a2a44 70%, #9ad43a); }
  .sleeve--kiwi  .sleeve__fruit { background: linear-gradient(180deg, #d8323a, #8cb83a 35%, #c02a30 65%, #7fb83a); }

  .sleeve__wordmark {
    position: absolute; top: 248px; width: 100%; text-align: center;
    color: var(--accent); font-weight: 900; font-size: 40px; line-height: 0.95;
  }

  .sleeve__flavours {
    position: absolute; top: 372px; left: 0; width: 100%;
    display: flex; justify-content: space-between; padding: 0 8px;
  }
  .flavour-tag {
    background: var(--accent); color: var(--accent-text);
    font-weight: 800; font-size: 10px; padding: 4px 6px; letter-spacing: 0.5px;
  }

  .sleeve__descriptor {
    position: absolute; top: 498px; width: 100%; text-align: center;
    color: var(--white); font-weight: 800; font-size: 13px; letter-spacing: 0.3px;
  }
  .sleeve__descriptor .energy { color: var(--accent); }

  .sleeve__volume {
    position: absolute; top: 519px; width: 100%; text-align: center;
    color: var(--muted); font-weight: 600; font-size: 7px;
  }
  .sleeve__volume .main { color: var(--white); font-size: 8px; margin: 0 4px; }

  .sleeve__swatch {
    position: absolute; top: 538px; left: 96px; width: 20px; height: 18px;
    background: var(--accent); border-radius: 2px;
  }
</style>
</head>
<body>

  <div class="brand-mark">COPPER<br>WREN</div>

  <section class="sleeve sleeve--mango">
    <p class="sleeve__tagline">COPPER WREN<br>FROM THE<br>COMPETITION</p>
    <div class="sleeve__fruit" role="img" aria-label="Photographic stack of mango and pineapple slices"></div>
    <p class="sleeve__wordmark">COPPER<br>WREN</p>
    <div class="sleeve__flavours"><span class="flavour-tag">MANGO</span><span class="flavour-tag">PINEAPPLE</span></div>
    <p class="sleeve__descriptor">NATURAL <span class="energy">ENERGY</span> DRINK</p>
    <p class="sleeve__volume">made from concentrate<span class="main">500 mL (17.6 fl oz)</span>fait de concentré</p>
    <div class="sleeve__swatch"></div>
  </section>

  <section class="sleeve sleeve--berry">
    <p class="sleeve__tagline">COPPER WREN<br>FROM THE<br>COMPETITION</p>
    <div class="sleeve__fruit" role="img" aria-label="Photographic stack of lime slices and blackberries"></div>
    <p class="sleeve__wordmark">COPPER<br>WREN</p>
    <div class="sleeve__flavours"><span class="flavour-tag">LIME</span><span class="flavour-tag">BLACKBERRY</span></div>
    <p class="sleeve__descriptor">NATURAL <span class="energy">ENERGY</span> DRINK</p>
    <p class="sleeve__volume">made from concentrate<span class="main">500 mL (17.6 fl oz)</span>fait de concentré</p>
    <div class="sleeve__swatch"></div>
  </section>

  <section class="sleeve sleeve--kiwi">
    <p class="sleeve__tagline">COPPER WREN<br>FROM THE<br>COMPETITION</p>
    <div class="sleeve__fruit" role="img" aria-label="Photographic stack of kiwi slices and strawberries"></div>
    <p class="sleeve__wordmark">COPPER<br>WREN</p>
    <div class="sleeve__flavours"><span class="flavour-tag">KIWI</span><span class="flavour-tag">STRAWBERRY</span></div>
    <p class="sleeve__descriptor">NATURAL <span class="energy">ENERGY</span> DRINK</p>
    <p class="sleeve__volume">made from concentrate<span class="main">500 mL (17.6 fl oz)</span>fait de concentré</p>
    <div class="sleeve__swatch"></div>
  </section>

</body>
</html>
```